Zielgruppe
Elektro und Automatisierungstechnik
Zielgruppe: Industriekunden
Aufgabenstellung
Zweiseitig farbig
Querformat 8,5*5,5cm
modernes, innovatives und zuverlässiges Unternehmen
Vorhandenes Logo muss integriert werden. Siehe Anhang

```html
<!DOCTYPE html>
<html lang="de">
<head>
<meta charset="utf-8">
<title>Kolsin Elektrotechnik – Visitenkarte</title>
<link rel="stylesheet" href="https://fonts.googleapis.com/css2?family=Exo+2:wght@500;600&display=swap">
<style>
  :root {
    --stage: #e4e4e4;
    --card: #ffffff;
    --navy: #183856;
    --ink: #2b2b2b;
  }
  html, body {
    margin: 0;
    width: 1200px;
    height: 1200px;
    overflow: hidden;
    background: var(--stage);
  }
  .card {
    position: absolute;
    left: 253px;
    width: 680px;
    height: 440px;
    background: var(--card);
    overflow: hidden;
  }
  .card--front { top: 123px; }
  .card--back { top: 620px; }

  .rule {
    position: absolute;
    left: 0;
    width: 100%;
    height: 6px;
    background: var(--ink);
  }
  .band {
    position: absolute;
    right: 0;
    width: 260px;
    background: var(--navy);
  }
  .card--front .rule { top: 272px; }
  .card--front .band { top: 288px; height: 40px; }
  .card--back .rule { top: 418px; }
  .card--back .band { top: 430px; height: 10px; }

  .brand {
    position: absolute;
    display: flex;
    align-items: flex-start;
    gap: 14px;
    font-family: "Exo 2", sans-serif;
    text-transform: uppercase;
    line-height: 1;
  }
  .card--front .brand { left: 43px; top: 119px; }
  .card--back .brand { left: 167px; top: 189px; }
  .brand__mark {
    width: 18px;
    height: 18px;
    background: var(--navy);
    margin-top: 8px;
  }
  .brand__name {
    display: block;
    font-size: 56px;
    font-weight: 600;
    letter-spacing: 8px;
    color: var(--navy);
  }
  .brand__field {
    display: block;
    margin-top: 8px;
    font-size: 24px;
    font-weight: 500;
    letter-spacing: 3px;
    color: var(--ink);
  }
</style>
</head>
<body>
  <section class="card card--front">
    <div class="rule"></div>
    <div class="band"></div>
    <div class="brand">
      <span class="brand__mark"></span>
      <div class="brand__text">
        <span class="brand__name">Kolsin</span>
        <span class="brand__field">Elektrotechnik</span>
      </div>
    </div>
  </section>

  <section class="card card--back">
    <div class="rule"></div>
    <div class="band"></div>
    <div class="brand">
      <span class="brand__mark"></span>
      <div class="brand__text">
        <span class="brand__name">Kolsin</span>
        <span class="brand__field">Elektrotechnik</span>
      </div>
    </div>
  </section>
</body>
</html>
```